We would like a business card that includes our logo on the front and the following information on the back:

Warren Pike, Owner
Phone: (555) 614-0827
email: wpikefencing@brookmail.example

Wally Pike & Sons Fencing provides the following services:
Barbed wire
Smooth wire
High tensile
Electric

On the bottom of the card please add:
Please call or email Warren for estimates.

```html
<!DOCTYPE html>
<html lang="en">
<head>
<meta charset="utf-8">
<title>Wally Pike &amp; Sons Fencing – Business Card</title>
<link rel="stylesheet" href="https://fonts.googleapis.com/css2?family=Cinzel:wght@600;700&family=Montserrat:wght@400;500&display=swap">
<style>
  :root {
    --backdrop: #c9c9c9;
    --card-white: #ffffff;
    --card-dark: #2b2322;
    --brand-brown: #7a5a40;
    --ink: #2b2322;
    --light-text: #f4efea;
  }
  * { box-sizing: border-box; margin: 0; padding: 0; }
  html, body { width: 1200px; height: 788px; overflow: hidden; }
  body {
    background: var(--backdrop);
    font-family: "Montserrat", sans-serif;
    color: var(--ink);
    position: relative;
  }
  .card {
    position: absolute;
    width: 540px;
    height: 310px;
    border-radius: 22px;
    overflow: hidden;
    box-shadow: 0 10px 24px rgba(0,0,0,.22);
  }
  /* Contact side */
  .card-back { left: 40px; top: 80px; background: var(--card-white); }
  .card-back .graphics { position: absolute; inset: 0; }
  .brand-block {
    position: absolute; right: 34px; top: 26px;
    display: flex; align-items: center; gap: 12px;
  }
  .brand-dot { width: 26px; height: 26px; border-radius: 50%; background: var(--brand-brown); }
  .brand-name {
    font-family: "Cinzel", serif; font-weight: 700;
    font-size: 19px; line-height: 1.15; color: var(--ink); text-align: right;
  }
  .services {
    position: absolute; right: 34px; top: 104px;
    text-align: right; font-size: 11.5px; line-height: 1.45;
  }
  .services-intro { margin-bottom: 4px; }
  .services-list { list-style: none; }
  .services-list li::after {
    content: ""; display: inline-block; width: 4px; height: 4px;
    border-radius: 50%; background: var(--brand-brown);
    margin-left: 4px; vertical-align: middle;
  }
  .person { position: absolute; left: 34px; top: 148px; }
  .person-name { font-family: "Cinzel", serif; font-weight: 700; font-size: 22px; letter-spacing: .5px; }
  .person-role { font-size: 12px; margin-top: 2px; }
  .contacts { position: absolute; left: 34px; top: 204px; list-style: none; font-size: 12.5px; line-height: 1.5; }
  .contacts li { display: flex; align-items: center; gap: 8px; }
  .contacts svg { width: 11px; height: 11px; fill: var(--brand-brown); flex: none; }
  .footer-note {
    position: absolute; left: 34px; bottom: 12px;
    font-size: 12.5px; color: var(--light-text); letter-spacing: .2px;
  }
  /* Logo side */
  .card-front {
    left: 620px; top: 398px; background: var(--card-dark);
    display: flex; flex-direction: column; align-items: center; justify-content: center; gap: 18px;
  }
  .front-dot { width: 64px; height: 64px; border-radius: 50%; background: var(--brand-brown); }
  .front-name {
    font-family: "Cinzel", serif; font-weight: 700; color: var(--light-text);
    font-size: 34px; line-height: 1.15; text-align: center;
  }
</style>
</head>
<body>

<section class="card card-back" aria-label="Business card, contact side">
  <svg class="graphics" viewBox="0 0 540 310" aria-hidden="true">
    <polyline points="34,198 278,198 302,94 540,94" fill="none" stroke="var(--brand-brown)" stroke-width="1"/>
    <rect x="300" y="248" width="240" height="5" fill="var(--brand-brown)"/>
    <path d="M0,272 L290,272 Q300,258 315,258 L540,258 L540,310 L0,310 Z" fill="var(--card-dark)"/>
  </svg>

  <div class="brand-block">
    <div class="brand-name">Wally Pike &amp; Sons<br>Fencing</div>
    <span class="brand-dot"></span>
  </div>

  <div class="services">
    <p class="services-intro">Wally Pike &amp; Sons Fencing<br>provides the following services:</p>
    <ul class="services-list">
      <li>Barbed wire</li>
      <li>Smooth wire</li>
      <li>High tensile</li>
      <li>Electric</li>
    </ul>
  </div>

  <div class="person">
    <p class="person-name">WARREN PIKE</p>
    <p class="person-role">Owner</p>
  </div>

  <ul class="contacts">
    <li><svg viewBox="0 0 12 12"><path d="M2.5 1 L4.5 1 L5.3 3.5 L4 4.5 Q5 6.8 7.5 8 L8.5 6.7 L11 7.5 L11 9.5 Q10.5 11 9 11 Q1 10 1 2.8 Q1 1 2.5 1 Z"/></svg>(555) 614-0827</li>
    <li><svg viewBox="0 0 12 12"><path d="M0 2 H12 V10 H0 Z M0.8 2.6 L6 6.6 L11.2 2.6" stroke="#fff" stroke-width=".8"/></svg>wpikefencing@brookmail.example</li>
    <li><svg viewBox="0 0 12 12"><circle cx="6" cy="6" r="5.5"/></svg>www.wpikefencing.example</li>
  </ul>

  <p class="footer-note">Please call or email Warren for estimates.</p>
</section>

<section class="card card-front" aria-label="Business card, logo side">
  <span class="front-dot"></span>
  <p class="front-name">Wally Pike &amp; Sons<br>Fencing</p>
</section>

</body>
</html>
```